Minimalist Modern Business Card Design, open to ideas, or cleaner version of provided files, but what logo & logo colors (with some black) as shown in files, and info for back shown in files as well.

```html
<!DOCTYPE html>
<html lang="en">
<head>
<meta charset="utf-8">
<title>Mobile Rig Care – Business Card</title>
<link href="https://fonts.googleapis.com/css2?family=Montserrat:wght@400;600;700&display=swap" rel="stylesheet">
<style>
  :root {
    --navy: #262669;
    --ink: #1c1c1c;
    --paper: #ffffff;
    --backdrop: #3a3a3a;
  }
  * { box-sizing: border-box; margin: 0; padding: 0; }
  html, body { width: 1200px; height: 1200px; overflow: hidden; }
  body {
    background: var(--backdrop);
    font-family: "Montserrat", sans-serif;
    position: relative;
  }
  .card {
    position: absolute;
    left: 220px;
    width: 760px;
    height: 434px;
    border-radius: 26px;
    overflow: hidden;
  }
  .card-back { top: 126px; background: var(--navy); }
  .card-front { top: 640px; background: var(--paper); }

  .back-brand {
    position: absolute;
    left: 150px;
    top: 150px;
    display: flex;
    align-items: center;
    gap: 48px;
  }
  .brand-square {
    width: 110px;
    height: 110px;
    background: var(--paper);
  }
  .back-name {
    color: var(--paper);
    font-weight: 600;
    font-size: 58px;
    line-height: 1.02;
  }

  .front-name {
    position: absolute;
    left: 44px;
    top: 44px;
    color: var(--navy);
    font-weight: 600;
    font-size: 56px;
    line-height: 1.02;
  }
  .front-square {
    position: absolute;
    right: 60px;
    top: 60px;
    width: 250px;
    height: 250px;
    background: var(--navy);
  }
  .person {
    position: absolute;
    left: 44px;
    top: 206px;
  }
  .person-name {
    color: var(--navy);
    font-weight: 700;
    font-size: 24px;
  }
  .person-role {
    color: var(--ink);
    font-size: 15px;
    margin-top: 2px;
  }
  .address {
    color: var(--ink);
    font-size: 15px;
    line-height: 1.4;
    margin-top: 14px;
  }
  .contacts {
    list-style: none;
    margin-top: 14px;
  }
  .contacts li {
    display: flex;
    align-items: center;
    gap: 12px;
    color: var(--ink);
    font-size: 15px;
    line-height: 1.75;
  }
  .contacts svg { width: 16px; height: 16px; fill: var(--navy); flex: none; }
</style>
</head>
<body>
  <section class="card card-back">
    <div class="back-brand">
      <div class="brand-square"></div>
      <div class="back-name">Mobile<br>Rig Care</div>
    </div>
  </section>

  <section class="card card-front">
    <div class="front-name">Mobile<br>Rig Care</div>
    <div class="front-square"></div>

    <div class="person">
      <div class="person-name">Daniel Reyes</div>
      <div class="person-role">President</div>
      <div class="address">4180 Harbor Ridge Ave<br>Suite 210 Lakeview CO 80519</div>
      <ul class="contacts">
        <li>
          <svg viewBox="0 0 16 16" aria-hidden="true"><path d="M3 2h3l1.5 3.5-2 1.3a8 8 0 0 0 3.7 3.7l1.3-2L14 10v3a1 1 0 0 1-1 1A11 11 0 0 1 2 3a1 1 0 0 1 1-1z"/></svg>
          555-014-2290
        </li>
        <li>
          <svg viewBox="0 0 16 16" aria-hidden="true"><path d="M1 3h14v10H1z M1.5 3.5 8 9l6.5-5.5" stroke="#fff" stroke-width="1.2"/></svg>
          hello@mobilerigcare.com
        </li>
        <li>
          <svg viewBox="0 0 16 16" aria-hidden="true"><circle cx="8" cy="8" r="7"/><path d="M1 8h14M8 1c-3 3.5-3 10.5 0 14M8 1c3 3.5 3 10.5 0 14" stroke="#fff" stroke-width="1" fill="none"/></svg>
          www.mobilerigcare.com
        </li>
      </ul>
    </div>
  </section>
</body>
</html>
```